Velmora Training Clinical Treatments workbook New Word Template Design Project

Velmora Training needs the old "Tallowind Aesthetics Clinical Treatments Workbook" updated and given a fresh new look, using the new Velmora Training logo.

The old workbook will be supplied to act as a guideline, but we'd like a fresh new look.

Target Market(s)

The people using this workbook are Dermal therapists and Dermal nurses.

Font styles to use
Serif
Sans Serif

Requirements
Must have
• The new logo incorporated on each page - obviously on the cover it will be a major focus, but on other pages we'd like to see the logo represented in a smaller way somehow.

Each module is to follow the same formula - as per the old workbook.

A4 portrait - 210mm X 297mm (8-1/4 X 11-3/4 inches)

The end result will be printed, so there must be space on the LH side to allow for binding
Nice to have
• We'd like the colour scheme of the new design to work in/match with the colour scheme of the logo.

Request from my boss - the final products we will need back are:
(1) an editable "in design" file
(2) pdf document

```html
<!DOCTYPE html>
<html lang="en">
<head>
<meta charset="utf-8">
<title>Velmora Training – Clinical Treatments Workbook Spreads</title>
<link href="https://fonts.googleapis.com/css2?family=Oswald:wght@400;500&family=Cormorant+Garamond:wght@600&family=Open+Sans:wght@400;600;700&display=swap" rel="stylesheet">
<style>
:root{
  --bg:#e6e6e6;
  --paper:#ffffff;
  --navy:#1f2a5c;
  --ink:#3a3f5c;
  --gold:#e2a829;
  --orange:#f2a23a;
  --cream:#fbf0d9;
  --line:#c3c7d3;
  --grey-box:#ececef;
}
*{box-sizing:border-box;margin:0;padding:0}
html,body{width:1200px;height:1200px;overflow:hidden;background:var(--bg);font-family:"Open Sans",sans-serif}
.row{position:absolute;left:32px;display:flex;gap:18px}
.page{width:126px;height:160px;background:var(--paper);box-shadow:0 2px 5px rgba(0,0,0,.18);position:relative;overflow:hidden;padding:8px 9px 0 13px;font-size:2.7px;line-height:1.5;color:var(--ink)}
.head{display:flex;justify-content:space-between;align-items:flex-start;height:11px;gap:3px}
.page-title{font-family:"Oswald",sans-serif;font-size:4.3px;color:var(--navy);white-space:nowrap;text-transform:uppercase}
.brand{display:flex;align-items:center;gap:1.5px;font-family:"Cormorant Garamond",serif;font-weight:600;font-size:3.4px;color:var(--navy);letter-spacing:.3px;text-transform:uppercase;white-space:nowrap}
.brand-dot{width:4px;height:4px;border-radius:50%;background:var(--navy)}
.foot{position:absolute;right:9px;bottom:6px;display:flex;gap:1px}
.foot .n{width:19px;height:3.4px;background:var(--navy);color:#fff;font-size:2px;line-height:3.4px;text-align:center}
.foot .g{width:4px;height:3.4px;background:var(--gold)}
.num{font-family:"Oswald",sans-serif;font-size:12px;color:var(--orange);line-height:1}
.mod-title{font-family:"Oswald",sans-serif;font-size:4.6px;color:var(--navy);text-transform:uppercase;margin:3px 0 3px;line-height:1.2}
.bullets{list-style:none}
.bullets li{position:relative;padding-left:4px;margin-bottom:2px}
.bullets li::before{content:"";position:absolute;left:.5px;top:1.4px;width:1.4px;height:1.4px;border-radius:50%;background:var(--navy)}
.howto{background:var(--cream);padding:3px 4px;margin-top:4px}
.howto h4{font-family:"Oswald",sans-serif;font-weight:500;font-size:3.4px;color:var(--navy);margin-bottom:1px;text-transform:uppercase}
.howto ol{padding-left:4px}
.staff{font-size:2.5px;color:var(--navy);font-weight:700;text-transform:uppercase;margin-top:1px}
.sub{font-size:2.6px;color:var(--navy);font-weight:600;margin-top:1px}
table.sheet{width:100%;border-collapse:collapse;font-size:2.2px;margin-top:3px;line-height:1.2}
.sheet th{font-weight:700;color:var(--navy);border:.4px solid var(--line);padding:.8px 1px;text-align:left;background:var(--cream)}
.sheet td{border:.4px solid var(--line);height:4.2px;padding:0 1px}
.sheet td:first-child{color:var(--orange);font-weight:600;width:20px}
.yn td:first-child{color:var(--ink);font-weight:400;width:auto}
.yn td+td,.yn th+th{width:6px;text-align:center}
.yn td{height:3.6px}
.checks{margin-top:3px;font-size:2.4px}
.checks p{display:flex;justify-content:space-between;color:var(--navy);font-weight:600}
.signbox{background:var(--grey-box);padding:2px 3px;margin-top:4px;font-size:2.3px;color:var(--navy)}
.toc{list-style:none;margin-top:4px;font-size:2.5px}
.toc li{display:flex;gap:3px;line-height:1.75}
.toc .m{color:var(--orange);font-weight:600;width:14px}
.toc .t{flex:1;color:var(--navy)}
.sum{width:100%;border-collapse:collapse;font-size:2.3px;margin-top:4px;line-height:1.2}
.sum th,.sum td{border:.5px solid var(--navy);padding:1px 1.5px;text-align:left;color:var(--navy)}
.sum td:first-child{color:var(--orange);font-weight:600}
.cover{padding:0;text-align:center}
.cover .mark{width:24px;height:24px;margin:18px auto 3px;background:var(--navy);border-radius:4px}
.cover .brand{justify-content:center;font-size:4.6px}
.cover h1{font-family:"Oswald",sans-serif;font-weight:400;font-size:8.4px;color:var(--navy);line-height:1.25;margin-top:10px;text-transform:uppercase}
.cover .staff-l{font-size:3px;color:var(--navy);margin-top:8px}
.cover .staff-line{width:60px;height:.6px;background:var(--navy);margin:6px auto 0}
.cover svg{position:absolute;left:0;bottom:0}
.end h1{font-size:7px;margin-top:8px}
.end p{font-size:2.8px;color:var(--navy);margin:3px 16px 0;line-height:1.45}
</style>
</head>
<body>

<!-- ROW 1 -->
<div class="row" style="top:44px">
  <div class="page cover">
    <div class="mark" role="img" aria-label="Velmora Training emblem area"></div>
    <div class="brand"><span>Velmora Training</span></div>
    <h1>Clinical<br>Treatments Workbook</h1>
    <div class="staff-l">STAFF NAME:</div>
    <div class="staff-line"></div>
    <svg width="126" height="60" viewBox="0 0 126 60"><path d="M0 22 Q60 52 126 10 V60 H0Z" fill="var(--gold)"/><path d="M0 32 Q62 60 126 20 V60 H0Z" fill="var(--navy)"/></svg>
  </div>

  <div class="page"><div class="head"><span class="page-title">Table of Contents</span><span class="brand"><i class="brand-dot"></i>Velmora Training</span></div>
    <ul class="toc">
      <li><span class="m"></span><span class="t">Introduction</span><span>3</span></li>
      <li><span class="m"></span><span class="t">Workbook Summary</span><span>4</span></li>
      <li><span class="m">Module 01</span><span class="t">Documentation for Treatments</span><span>5</span></li>
      <li><span class="m">Module 02</span><span class="t">Medical Photography</span><span>8</span></li>
      <li><span class="m">Module 03</span><span class="t">Infection Prevention &amp; Control</span><span>11</span></li>
      <li><span class="m">Module 04</span><span class="t">Sterilisation</span><span>12</span></li>
      <li><span class="m">Module 05</span><span class="t">Workplace Maintenance</span><span>15</span></li>
      <li><span class="m">Module 06</span><span class="t">Pathology Collection</span><span>18</span></li>
      <li><span class="m">Module 07</span><span class="t">Drugs &amp; Poisons Regulation</span><span>21</span></li>
      <li><span class="m">Module 08</span><span class="t">Pre-Op Calls to Patients</span><span>22</span></li>
      <li><span class="m">Module 09</span><span class="t">Administering Numbing Cream</span><span>24</span></li>
      <li><span class="m">Module 10</span><span class="t">Following Up Post Treatment</span><span>27</span></li>
      <li><span class="m">Module 11</span><span class="t">Chemical Peels</span><span>29</span></li>
      <li><span class="m">Module 12</span><span class="t">Extractions</span><span>32</span></li>
      <li><span class="m">Module 13</span><span class="t">LED Treatment</span><span>34</span></li>
      <li><span class="m">Module 14</span><span class="t">Hair Removal</span><span>35</span></li>
      <li><span class="m">Module 15</span><span class="t">Broad Band Light</span><span>38</span></li>
      <li><span class="m">Module 16</span><span class="t">Fractionated Laser</span><span>40</span></li>
    </ul>
    <div class="foot"><span class="n">Page 1</span><span class="g"></span></div></div>

  <div class="page"><div class="head"><span class="page-title">Table of Contents</span><span class="brand"><i class="brand-dot"></i>Velmora Training</span></div>
    <ul class="toc">
      <li><span class="m">Form 01</span><span class="t">Treatment Audit Sheet</span><span>7</span></li>
      <li><span class="m">Form 02</span><span class="t">Photography Form</span><span>10</span></li>
      <li><span class="m">Form 03</span><span class="t">Sterilisation Form</span><span>14</span></li>
      <li><span class="m">Form 04</span><span class="t">Maintenance Form</span><span>17</span></li>
      <li><span class="m">Form 05</span><span class="t">Pathology Form</span><span>20</span></li>
      <li><span class="m">Form 06</span><span class="t">Numbing Cream Form</span><span>26</span></li>
      <li><span class="m">Form 07</span><span class="t">Chemical Peel Form</span><span>31</span></li>
      <li><span class="m">Form 08</span><span class="t">Hair Removal Form</span><span>37</span></li>
      <li><span class="m">Form 09</span><span class="t">Laser Forms</span><span>42</span></li>
      <li><span class="m"></span><span class="t">Completion</span><span>45</span></li>
    </ul>
    <div class="foot"><span class="n">Page 2</span><span class="g"></span></div></div>

  <div class="page"><div class="head"><span class="page-title">Introduction</span><span class="brand"><i class="brand-dot"></i>Velmora Training</span></div>
    <ul class="bullets">
      <li>Welcome to the clinical team. This workbook guides you through every treatment you will perform in the clinic.</li>
      <li>Each module explains the standard we expect and lists the steps needed to show you are competent.</li>
      <li>All of your clinical sheets must be kept in this workbook and reviewed by your trainer.</li>
      <li>Please ask your trainer if any part of a module is unclear before you begin treating clients.</li>
      <li>Refer to the Clinical Manual for full protocols, pricing and aftercare information.</li>
      <li>Progress is tracked on the summary page; your trainer will date each module once complete.</li>
    </ul>
    <div class="howto"><h4>How to finish this workbook</h4><ol><li>Read each module in order.</li><li>Complete every sign off sheet.</li><li>Have each page signed by your trainer.</li></ol></div>
    <div class="foot"><span class="n">Page 3</span><span class="g"></span></div></div>

  <div class="page"><div class="head"><span class="page-title">Workbook Summary</span><span class="brand"><i class="brand-dot"></i>Velmora Training</span></div>
    <table class="sum">
      <tr><th>Module</th><th>Title</th><th>Date Completed</th></tr>
      <tr><td>01</td><td>Documentation for Treatments</td><td></td></tr>
      <tr><td>02</td><td>Medical Photography</td><td></td></tr>
      <tr><td>03</td><td>Infection Prevention &amp; Control</td><td></td></tr>
      <tr><td>04</td><td>Sterilisation</td><td></td></tr>
      <tr><td>05</td><td>Workplace Maintenance</td><td></td></tr>
      <tr><td>06</td><td>Pathology Collection</td><td></td></tr>
      <tr><td>07</td><td>Drugs &amp; Poisons Regulation</td><td></td></tr>
      <tr><td>08</td><td>Pre-Op Calls to Patients</td><td></td></tr>
      <tr><td>09</td><td>Administering Numbing Cream</td><td></td></tr>
      <tr><td>10</td><td>Following Up Post Treatment</td><td></td></tr>
      <tr><td>11</td><td>Chemical Peels</td><td></td></tr>
      <tr><td>12</td><td>Extractions</td><td></td></tr>
      <tr><td>13</td><td>LED Treatment</td><td></td></tr>
      <tr><td>14</td><td>Hair Removal</td><td></td></tr>
      <tr><td>15</td><td>Broad Band Light</td><td></td></tr>
      <tr><td>16</td><td>Fractionated Laser</td><td></td></tr>
    </table>
    <div class="foot"><span class="n">Page 4</span><span class="g"></span></div></div>

  <div class="page"><div class="head"><span class="num">01</span><span class="brand"><i class="brand-dot"></i>Velmora Training</span></div>
    <div class="mod-title">Documentation for Treatments</div>
    <ul class="bullets">
      <li>Every treatment must be recorded in the client file on the same day it is performed.</li>
      <li>Notes must include the settings used, products applied and how the skin responded.</li>
      <li>Consent forms are signed before the first treatment and renewed each year.</li>
      <li>Your trainer will audit five of your client files during this module.</li>
    </ul>
    <div class="howto"><h4>How to finish this module</h4><ol><li>Read the manual section on documentation.</li><li>Watch the client records video.</li><li>Complete the sign off sheet for five clients.</li><li>Have your trainer complete the audit.</li></ol></div>
    <div class="foot"><span class="n">Page 5</span><span class="g"></span></div></div>

  <div class="page"><div class="head"><span class="num" style="font-size:7px">Module 1:</span><span class="brand"><i class="brand-dot"></i>Velmora Training</span></div>
    <div class="sub">Documentation sign off sheet</div><div class="staff">Staff Name:</div>
    <table class="sheet"><tr><th>Type</th><th>Date</th><th>Client File Reviewed</th><th>Trainer Sign</th></tr>
      <tr><td>Client 1</td><td></td><td></td><td></td></tr><tr><td>Client 2</td><td></td><td></td><td></td></tr><tr><td>Client 3</td><td></td><td></td><td></td></tr><tr><td>Client 4</td><td></td><td></td><td></td></tr><tr><td>Client 5</td><td></td><td></td><td></td></tr><tr><td>Client 6</td><td></td><td></td><td></td></tr><tr><td>Client 7</td><td></td><td></td><td></td></tr><tr><td>Client 8</td><td></td><td></td><td></td></tr><tr><td>Client 9</td><td></td><td></td><td></td></tr><tr><td>Client 10</td><td></td><td></td><td></td></tr><tr><td>Client 11</td><td></td><td></td><td></td></tr><tr><td>Client 12</td><td></td><td></td><td></td></tr>
    </table>
    <div class="checks"><p>Consent forms complete <span>Yes / No</span></p><p>Notes legible and dated <span>Yes / No</span></p><p>Aftercare recorded <span>Yes / No</span></p></div>
    <div class="signbox">Trainer: ____________ Date: ________</div>
    <div class="foot"><span class="n">Page 6</span><span class="g"></span></div></div>

  <div class="page"><div class="head"><span class="page-title">Treatment Audit Sheet</span><span class="brand"><i class="brand-dot"></i>Velmora Training</span></div>
    <table class="sheet yn"><tr><th>Audit item</th><th>Y</th><th>N</th></tr>
      <tr><td>Consent form signed and dated</td><td></td><td></td></tr><tr><td>Medical history updated</td><td></td><td></td></tr><tr><td>Skin type recorded</td><td></td><td></td></tr><tr><td>Settings and products noted</td><td></td><td></td></tr><tr><td>Skin response described</td><td></td><td></td></tr><tr><td>Aftercare given to client</td><td></td><td></td></tr><tr><td>Next visit booked</td><td></td><td></td></tr>
    </table>
    <div class="signbox">Trainer: ____________ Date: ________</div>
    <table class="sheet yn" style="margin-top:5px"><tr><th>Audit item</th><th>Y</th><th>N</th></tr>
      <tr><td>Consent form signed and dated</td><td></td><td></td></tr><tr><td>Medical history updated</td><td></td><td></td></tr><tr><td>Skin type recorded</td><td></td><td></td></tr><tr><td>Settings and products noted</td><td></td><td></td></tr><tr><td>Skin response described</td><td></td><td></td></tr><tr><td>Aftercare given to client</td><td></td><td></td></tr><tr><td>Next visit booked</td><td></td><td></td></tr>
    </table>
    <div class="signbox">Trainer: ____________ Date: ________</div>
    <div class="foot"><span class="n">Page 7</span><span class="g"></span></div></div>
</div>

<!-- ROW 2 -->
<div class="row" style="top:238px">
  <div class="page"><div class="head"><span class="num">02</span><span class="brand"><i class="brand-dot"></i>Velmora Training</span></div>
    <div class="mod-title">Medical Photography</div>
    <ul class="bullets">
      <li>Taking good medical photographs is an essential skill for tracking client results.</li>
      <li>Photos are taken before the first treatment and at every review appointment.</li>
      <li>Use the same lighting, angle and distance each time so results can be compared.</li>
      <li>Photos are stored only in the client file and never on personal devices.</li>
    </ul>
    <div class="howto"><h4>How to finish this module</h4><ol><li>Read the manual section on photography.</li><li>Watch the photography video.</li><li>Photograph three clients with your trainer.</li><li>Complete the sign off sheet.</li></ol></div>
    <div class="foot"><span class="n">Page 8</span><span class="g"></span></div></div>

  <div class="page"><div class="head"><span class="page-title">Photography Sign Off</span><span class="brand"><i class="brand-dot"></i>Velmora Training</span></div>
    <div class="staff">Staff Name:</div>
    <table class="sheet"><tr><th>Type</th><th>Date</th><th>Area Photographed</th><th>Trainer Sign</th></tr>
      <tr><td>Client 1</td><td></td><td></td><td></td></tr><tr><td>Client 2</td><td></td><td></td><td></td></tr><tr><td>Client 3</td><td></td><td></td><td></td></tr><tr><td>Client 4</td><td></td><td></td><td></td></tr><tr><td>Client 5</td><td></td><td></td><td></td></tr><tr><td>Client 6</td><td></td><td></td><td></td></tr><tr><td>Client 7</td><td></td><td></td><td></td></tr>
    </table>
    <div class="checks"><p>Confident taking photos <span>Yes / No</span></p><p>Confident uploading photos <span>Yes / No</span></p><p>Photos filed correctly <span>Yes / No</span></p></div>
    <div class="signbox">Trainer Name: ____________<br>Signature: ____________ Date: ______</div>
    <div class="foot"><span class="n">Page 9</span><span class="g"></span></div></div>

  <div class="page"><div class="head"><span class="page-title">Photography Form</span><span class="brand"><i class="brand-dot"></i>Velmora Training</span></div>
    <div class="staff">Client Name:</div>
    <table class="sheet yn"><tr><th>Checklist</th><th>Y</th><th>N</th></tr>
      <tr><td>Photo consent signed</td><td></td><td></td></tr><tr><td>Make-up removed</td><td></td><td></td></tr><tr><td>Hair tied back</td><td></td><td></td></tr><tr><td>Plain background used</td><td></td><td></td></tr><tr><td>Front view taken</td><td></td><td></td></tr><tr><td>Left side view taken</td><td></td><td></td></tr><tr><td>Right side view taken</td><td></td><td></td></tr><tr><td>Close up of concern</td><td></td><td></td></tr><tr><td>Photos uploaded to file</td><td></td><td></td></tr><tr><td>Camera wiped after use</td><td></td><td></td></tr>
    </table>
    <div class="checks"><p>Confident with lighting <span>Yes / No</span></p><p>Confident with angles <span>Yes / No</span></p></div>
    <div class="signbox">Trainer Name: ____________<br>Signature: ____________ Date: ______</div>
    <div class="foot"><span class="n">Page 10</span><span class="g"></span></div></div>

  <div class="page"><div class="head"><span class="num">03</span><span class="brand"><i class="brand-dot"></i>Velmora Training</span></div>
    <div class="mod-title">Infection Prevention &amp; Control</div>
    <ul class="bullets">
      <li>Good infection control protects every client and every member of the team.</li>
      <li>Wash hands before and after each client and whenever gloves are changed.</li>
      <li>Clean all surfaces and equipment between clients with approved wipes.</li>
    </ul>
    <div class="howto"><h4>How to finish this module</h4><ol><li>Read the manual section on infection control.</li><li>Complete the online hand hygiene course.</li><li>Attach your certificate to this page.</li></ol></div>
    <div class="tiny" style="margin-top:4px">I confirm I have read and understood the infection control policy.</div>
    <div class="signbox">Staff Signature: ____________ Date: ______</div>
    <div class="foot"><span class="n">Page 11</span><span class="g"></span></div></div>

  <div class="page"><div class="head"><span class="num">04</span><span class="brand"><i class="brand-dot"></i>Velmora Training</span></div>
    <div class="mod-title">Sterilisation</div>
    <ul class="bullets">
      <li>All reusable instruments are cleaned, packed and sterilised after each use.</li>
      <li>Each autoclave cycle is logged with the date, load and your initials.</li>
      <li>Check the indicator strip on every pack before it is opened.</li>
      <li>Never use a pack that is wet, torn or past its date.</li>
    </ul>
    <div class="howto"><h4>How to finish this module</h4><ol><li>Read the manual section on sterilisation.</li><li>Watch the autoclave video.</li><li>Run three cycles with your trainer.</li><li>Complete the sign off sheet.</li></ol></div>
    <div class="foot"><span class="n">Page 12</span><span class="g"></span></div></div>

  <div class="page"><div class="head"><span class="page-title">Sterilisation Sign Off</span><span class="brand"><i class="brand-dot"></i>Velmora Training</span></div>
    <div class="staff">Staff Name:</div>
    <table class="sheet"><tr><th>Cycle</th><th>Date</th><th>Load</th><th>Indicator</th><th>Sign</th></tr>
      <tr><td>Cycle 1</td><td></td><td></td><td></td><td></td></tr><tr><td>Cycle 2</td><td></td><td></td><td></td><td></td></tr><tr><td>Cycle 3</td><td></td><td></td><td></td><td></td></tr><tr><td>Cycle 4</td><td></td><td></td><td></td><td></td></tr><tr><td>Cycle 5</td><td></td><td></td><td></td><td></td></tr><tr><td>Cycle 6</td><td></td><td></td><td></td><td></td></tr><tr><td>Cycle 7</td><td></td><td></td><td></td><td></td></tr>
    </table>
    <div class="checks"><p>Confident cleaning tools <span>Yes / No</span></p><p>Confident packing tools <span>Yes / No</span></p><p>Confident running cycle <span>Yes / No</span></p><p>Confident reading log <span>Yes / No</span></p></div>
    <div class="signbox">Trainer Name: ____________<br>Signature: ____________ Date: ______</div>
    <div class="foot"><span class="n">Page 13</span><span class="g"></span></div></div>

  <div class="page"><div class="head"><span class="page-title">Sterilisation Form</span><span class="brand"><i class="brand-dot"></i>Velmora Training</span></div>
    <ul class="bullets"><li>Instruments rinsed</li><li>Ultrasonic cleaner used</li><li>Pouches sealed</li><li>Dates labelled</li></ul>
    <table class="sheet yn"><tr><th>Step</th><th>Y</th><th>N</th></tr>
      <tr><td>Gloves and apron worn</td><td></td><td></td></tr><tr><td>Instruments fully dry</td><td></td><td></td></tr><tr><td>Chamber loaded correctly</td><td></td><td></td></tr><tr><td>Cycle selected</td><td></td><td></td></tr><tr><td>Printout checked</td><td></td><td></td></tr><tr><td>Log book filled in</td><td></td><td></td></tr><tr><td>Packs stored dry</td><td></td><td></td></tr>
    </table>
    <div class="checks"><p>Confident performing cycle <span>Yes / No</span></p><p>Confident storing packs <span>Yes / No</span></p></div>
    <div class="foot"><span class="n">Page 14</span><span class="g"></span></div></div>

  <div class="page"><div class="head"><span class="num">05</span><span class="brand"><i class="brand-dot"></i>Velmora Training</span></div>
    <div class="mod-title">Workplace Maintenance</div>
    <ul class="bullets">
      <li>Treatment rooms are checked and restocked at the start and end of each day.</li>
      <li>Report any faulty equipment to the clinic manager straight away.</li>
      <li>Machines are cleaned and filters checked as listed in the weekly roster.</li>
    </ul>
    <div class="howto"><h4>How to finish this module</h4><ol><li>Read the manual section on maintenance.</li><li>Walk through the rooms with your trainer.</li><li>Complete the sign off sheet for one week.</li><li>Complete the maintenance form.</li></ol></div>
    <div class="foot"><span class="n">Page 15</span><span class="g"></span></div></div>
</div>

<!-- ROW 3 -->
<div class="row" style="top:440px">
  <div class="page"><div class="head"><span class="page-title">Maintenance Sign Off</span><span class="brand"><i class="brand-dot"></i>Velmora Training</span></div>
    <div class="staff">Staff Name:</div>
    <table class="sheet"><tr><th>Day</th><th>Room</th><th>Tasks Done</th><th>Sign</th></tr>
      <tr><td>Monday</td><td></td><td></td><td></td></tr><tr><td>Tuesday</td><td></td><td></td><td></td></tr><tr><td>Wednesday</td><td></td><td></td><td></td></tr><tr><td>Thursday</td><td></td><td></td><td></td></tr><tr><td>Friday</td><td></td><td></td><td></td></tr><tr><td>Saturday</td><td></td><td></td><td></td></tr><tr><td>Sunday</td><td></td><td></td><td></td></tr>
    </table>
    <div class="checks"><p>Rooms restocked <span>Yes / No</span></p><p>Machines cleaned <span>Yes / No</span></p><p>Faults reported <span>Yes / No</span></p><p>Bins emptied <span>Yes / No</span></p></div>
    <div class="signbox">Trainer Name: ____________<br>Signature: ____________ Date: ______</div>
    <div class="foot"><span class="n">Page 16</span><span class="g"></span></div></div>

  <div class="page"><div class="head"><span class="page-title">Maintenance Form</span><span class="brand"><i class="brand-dot"></i>Velmora Training</span></div>
    <table class="sheet yn"><tr><th>Task</th><th>Y</th><th>N</th></tr>
      <tr><td>Couch roll replaced</td><td></td><td></td></tr><tr><td>Trolley wiped down</td><td></td><td></td></tr><tr><td>Towels restocked</td><td></td><td></td></tr><tr><td>Gloves restocked</td><td></td><td></td></tr><tr><td>Sharps bin checked</td><td></td><td></td></tr><tr><td>Machine filters checked</td><td></td><td></td></tr><tr><td>Fridge temperature logged</td><td></td><td></td></tr><tr><td>Floor cleaned</td><td></td><td></td></tr><tr><td>Lights and power off</td><td></td><td></td></tr>
    </table>
    <div class="checks"><p>Confident with roster <span>Yes / No</span></p><p>Confident reporting faults <span>Yes / No</span></p></div>
    <div class="signbox">Trainer Name: ____________<br>Signature: ____________ Date: ______</div>
    <div class="foot"><span class="n">Page 17</span><span class="g"></span></div></div>

  <div class="page"><div class="head"><span class="num">06</span><span class="brand"><i class="brand-dot"></i>Velmora Training</span></div>
    <div class="mod-title">Pathology Collection</div>
    <ul class="bullets">
      <li>Some treatments need blood or skin samples to be sent for testing.</li>
      <li>Label every sample with the client name, date of birth and date taken.</li>
    </ul>
    <div class="howto"><h4>How to finish this module</h4><ol><li>Read the manual section on pathology.</li><li>Watch the sample handling video.</li><li>Complete the sign off sheet.</li><li>Complete the pathology form.</li></ol></div>
    <div class="foot"><span class="n">Page 18</span><span class="g"></span></div></div>

  <div class="page"><div class="head"><span class="page-title">Pathology Sign Off</span><span class="brand"><i class="brand-dot"></i>Velmora Training</span></div>
    <div class="staff">Staff Name:</div>
    <table class="sheet"><tr><th>Type</th><th>Date</th><th>Sample Type</th><th>Trainer Sign</th></tr>
      <tr><td>Sample 1</td><td></td><td></td><td></td></tr><tr><td>Sample 2</td><td></td><td></td><td></td></tr><tr><td>Sample 3</td><td></td><td></td><td></td></tr><tr><td>Sample 4</td><td></td><td></td><td></td></tr><tr><td>Sample 5</td><td></td><td></td><td></td></tr><tr><td>Sample 6</td><td></td><td></td><td></td></tr><tr><td>Sample 7</td><td></td><td></td><td></td></tr>
    </table>
    <div class="checks"><p>Sample labelled correctly <span>Yes / No</span></p><p>Request form complete <span>Yes / No</span></p><p>Courier booked <span>Yes / No</span></p><p>Result filed <span>Yes / No</span></p></div>
    <div class="signbox">Trainer Name: ____________<br>Signature: ____________ Date: ______</div>
    <div class="foot"><span class="n">Page 19</span><span class="g"></span></div></div>

  <div class="page"><div class="head"><span class="page-title">Pathology Form</span><span class="brand"><i class="brand-dot"></i>Velmora Training</span></div>
    <ul class="bullets"><li>Client identity checked</li><li>Request form ready</li><li>Correct tubes chosen</li></ul>
    <table class="sheet yn"><tr><th>Step</th><th>Y</th><th>N</th></tr>
      <tr><td>Hands washed, gloves on</td><td></td><td></td></tr><tr><td>Site cleaned</td><td></td><td></td></tr><tr><td>Sample collected</td><td></td><td></td></tr><tr><td>Tube labelled</td><td></td><td></td></tr><tr><td>Bag sealed</td><td></td><td></td></tr><tr><td>Stored in fridge</td><td></td><td></td></tr>
    </table>
    <div class="checks"><p>Confident collecting <span>Yes / No</span></p><p>Confident labelling <span>Yes / No</span></p></div>
    <div class="signbox">Trainer Name: ____________<br>Signature: ____________ Date: ______</div>
    <div class="foot"><span class="n">Page 20</span><span class="g"></span></div></div>

  <div class="page"><div class="head"><span class="num">07</span><span class="brand"><i class="brand-dot"></i>Velmora Training</span></div>
    <div class="mod-title">Drugs &amp; Poisons Regulation</div>
    <ul class="bullets">
      <li>Scheduled products are stored in a locked cabinet with a signed register.</li>
      <li>Only trained staff may handle or record these products.</li>
    </ul>
    <div class="howto"><h4>How to finish this module</h4><ol><li>Read the manual section on scheduled products.</li><li>Review the register with your trainer.</li><li>Sign the declaration below.</li></ol></div>
    <ul class="bullets" style="margin-top:4px"><li>I have read the storage and register policy.</li><li>I know where the cabinet key is kept.</li><li>I will report any missing stock at once.</li></ul>
    <div class="signbox">Staff Signature: ____________ Date: ______</div>
    <div class="foot"><span class="n">Page 21</span><span class="g"></span></div></div>

  <div class="page"><div class="head"><span class="num">08</span><span class="brand"><i class="brand-dot"></i>Velmora Training</span></div>
    <div class="mod-title">Pre-Op Calls to Patients</div>
    <ul class="bullets">
      <li>Clients are called two days before surgery to confirm the time and answer questions.</li>
      <li>Remind clients about fasting, medication and transport home.</li>
      <li>Record the call and any concerns in the client file.</li>
    </ul>
    <div class="howto"><h4>How to finish this module</h4><ol><li>Read the manual section on pre-op calls.</li><li>Listen to two calls made by your trainer.</li><li>Make five calls and record them.</li><li>Complete the sign off sheet.</li></ol></div>
    <div class="foot"><span class="n">Page 22</span><span class="g"></span></div></div>

  <div class="page"><div class="head"><span class="page-title">Pre-Op Call Sign Off</span><span class="brand"><i class="brand-dot"></i>Velmora Training</span></div>
    <div class="staff">Staff Name:</div>
    <table class="sheet"><tr><th>Type</th><th>Date</th><th>Notes</th><th>Trainer Sign</th></tr>
      <tr><td>Call 1</td><td></td><td></td><td></td></tr><tr><td>Call 2</td><td></td><td></td><td></td></tr><tr><td>Call 3</td><td></td><td></td><td></td></tr><tr><td>Call 4</td><td></td><td></td><td></td></tr><tr><td>Call 5</td><td></td><td></td><td></td></tr><tr><td>Call 6</td><td></td><td></td><td></td></tr><tr><td>Call 7</td><td></td><td></td><td></td></tr>
    </table>
    <div class="checks"><p>Confident making calls <span>Yes / No</span></p><p>Calls recorded in file <span>Yes / No</span></p></div>
    <div class="signbox">Trainer Name: ____________<br>Signature: ____________ Date: ______</div>
    <div class="foot"><span class="n">Page 23</span><span class="g"></span></div></div>
</div>

<!-- ROW 4 -->
<div class="row" style="top:624px">
  <div class="page"><div class="head"><span class="num">09</span><span class="brand"><i class="brand-dot"></i>Velmora Training</span></div>
    <div class="mod-title">Administering Numbing Cream</div>
    <ul class="bullets">
      <li>Numbing cream is applied before some treatments to keep clients comfortable.</li>
      <li>Check allergies and record the amount and time applied.</li>
      <li>Remove all cream fully before the treatment begins.</li>
    </ul>
    <div class="howto"><h4>How to finish this module</h4><ol><li>Read the manual section on numbing cream.</li><li>Watch the application video.</li><li>Apply cream for five clients.</li><li>Complete the sign off sheet.</li></ol></div>
    <div class="foot"><span class="n">Page 24</span><span class="g"></span></div></div>

  <div class="page"><div class="head"><span class="page-title">Numbing Cream Sign Off</span><span class="brand"><i class="brand-dot"></i>Velmora Training</span></div>
    <div class="staff">Staff Name:</div>
    <table class="sheet"><tr><th>Type</th><th>Date</th><th>Area</th><th>Time On</th><th>Sign</th></tr>
      <tr><td>Client 1</td><td></td><td></td><td></td><td></td></tr><tr><td>Client 2</td><td></td><td></td><td></td><td></td></tr><tr><td>Client 3</td><td></td><td></td><td></td><td></td></tr><tr><td>Client 4</td><td></td><td></td><td></td><td></td></tr><tr><td>Client 5</td><td></td><td></td><td></td><td></td></tr><tr><td>Client 6</td><td></td><td></td><td></td><td></td></tr><tr><td>Client 7</td><td></td><td></td><td></td><td></td></tr>
    </table>
    <div class="checks"><p>Confident applying cream <span>Yes / No</span></p><p>Confident removing cream <span>Yes / No</span></p></div>
    <div class="signbox">Trainer Name: ____________<br>Signature: ____________ Date: ______</div>
    <div class="foot"><span class="n">Page 25</span><span class="g"></span></div></div>

  <div class="page"><div class="head"><span class="page-title">Numbing Cream Form</span><span class="brand"><i class="brand-dot"></i>Velmora Training</span></div>
    <table class="sheet yn"><tr><th>Step</th><th>Y</th><th>N</th></tr>
      <tr><td>Allergies checked</td><td></td><td></td></tr><tr><td>Skin cleansed</td><td></td><td></td></tr><tr><td>Cream applied evenly</td><td></td><td></td></tr><tr><td>Area covered with film</td><td></td><td></td></tr><tr><td>Time recorded</td><td></td><td></td></tr><tr><td>Cream removed fully</td><td></td><td></td></tr>
    </table>
    <div class="tiny">Client: __________ Date: ______</div>
    <table class="sheet yn" style="margin-top:4px"><tr><th>Step</th><th>Y</th><th>N</th></tr>
      <tr><td>Allergies checked</td><td></td><td></td></tr><tr><td>Skin cleansed</td><td></td><td></td></tr><tr><td>Cream applied evenly</td><td></td><td></td></tr><tr><td>Area covered with film</td><td></td><td></td></tr><tr><td>Time recorded</td><td></td><td></td></tr><tr><td>Cream removed fully</td><td></td><td></td></tr>
    </table>
    <div class="tiny">Client: __________ Date: ______</div>
    <div class="foot"><span class="n">Page 26</span><span class="g"></span></div></div>

  <div class="page"><div class="head"><span class="num">10</span><span class="brand"><i class="brand-dot"></i>Velmora Training</span></div>
    <div class="mod-title">Following up your patients post treatment</div>
    <ul class="bullets">
      <li>Call each client the day after a new treatment to check on their skin.</li>
      <li>Note any redness, swelling or concerns and tell your trainer.</li>
      <li>Good follow up builds trust and keeps clients coming back.</li>
    </ul>
    <div class="howto"><h4>How to finish this module</h4><ol><li>Complete the sign off sheet for five calls.</li></ol></div>
    <div class="foot"><span class="n">Page 27</span><span class="g"></span></div></div>

  <div class="page"><div class="head"><span class="page-title">Follow Up Sign Off</span><span class="brand"><i class="brand-dot"></i>Velmora Training</span></div>
    <div class="staff">Staff Name:</div>
    <table class="sheet"><tr><th>Type</th><th>Date</th><th>Treatment</th><th>Outcome</th><th>Sign</th></tr>
      <tr><td>Client 1</td><td></td><td></td><td></td><td></td></tr><tr><td>Client 2</td><td></td><td></td><td></td><td></td></tr><tr><td>Client 3</td><td></td><td></td><td></td><td></td></tr><tr><td>Client 4</td><td></td><td></td><td></td><td></td></tr><tr><td>Client 5</td><td></td><td></td><td></td><td></td></tr><tr><td>Client 6</td><td></td><td></td><td></td><td></td></tr><tr><td>Client 7</td><td></td><td></td><td></td><td></td></tr><tr><td>Client 8</td><td></td><td></td><td></td><td></td></tr><tr><td>Client 9</td><td></td><td></td><td></td><td></td></tr>
    </table>
    <div class="checks"><p>Confident making calls <span>Yes / No</span></p><p>Issues passed to trainer <span>Yes / No</span></p></div>
    <div class="signbox">Trainer Name: ____________<br>Signature: ____________ Date: ______</div>
    <div class="foot"><span class="n">Page 28</span><span class="g"></span></div></div>

  <div class="page"><div class="head"><span class="num">11</span><span class="brand"><i class="brand-dot"></i>Velmora Training</span></div>
    <div class="mod-title">Chemical Peels</div>
    <ul class="bullets">
      <li>Chemical peels remove dead skin cells to improve tone and texture.</li>
      <li>Always patch test new clients at least two days before the first peel.</li>
      <li>Time each layer carefully and neutralise as the product guide states.</li>
      <li>Give written aftercare and advise daily sun protection.</li>
    </ul>
    <div class="howto"><h4>How to finish this module</h4><ol><li>Read the manual section on peels.</li><li>Complete the sign off sheet.</li><li>Complete the chemical peel form.</li></ol></div>
    <div class="foot"><span class="n">Page 29</span><span class="g"></span></div></div>

  <div class="page"><div class="head"><span class="page-title">Chemical Peels Sign Off</span><span class="brand"><i class="brand-dot"></i>Velmora Training</span></div>
    <div class="staff">Staff Name:</div>
    <table class="sheet"><tr><th>Type</th><th>Date</th><th>Peel</th><th>Layers</th><th>Sign</th></tr>
      <tr><td>Client 1</td><td></td><td></td><td></td><td></td></tr><tr><td>Client 2</td><td></td><td></td><td></td><td></td></tr><tr><td>Client 3</td><td></td><td></td><td></td><td></td></tr><tr><td>Client 4</td><td></td><td></td><td></td><td></td></tr><tr><td>Client 5</td><td></td><td></td><td></td><td></td></tr><tr><td>Client 6</td><td></td><td></td><td></td><td></td></tr><tr><td>Client 7</td><td></td><td></td><td></td><td></td></tr>
    </table>
    <div class="checks"><p>Patch test completed <span>Yes / No</span></p><p>Aftercare given <span>Yes / No</span></p></div>
    <div class="signbox">Trainer Name: ____________<br>Signature: ____________ Date: ______</div>
    <div class="foot"><span class="n">Page 30</span><span class="g"></span></div></div>

  <div class="page"><div class="head"><span class="page-title">Chemical Peel Form</span><span class="brand"><i class="brand-dot"></i>Velmora Training</span></div>
    <table class="sheet yn"><tr><th>Step</th><th>Y</th><th>N</th></tr>
      <tr><td>Consultation completed</td><td></td><td></td></tr><tr><td>Patch test recorded</td><td></td><td></td></tr><tr><td>Photos taken</td><td></td><td></td></tr><tr><td>Skin cleansed and prepped</td><td></td><td></td></tr><tr><td>Eyes and lips protected</td><td></td><td></td></tr><tr><td>Peel applied evenly</td><td></td><td></td></tr><tr><td>Timer used for each layer</td><td></td><td></td></tr><tr><td>Peel neutralised</td><td></td><td></td></tr><tr><td>Soothing mask applied</td><td></td><td></td></tr><tr><td>Sunscreen applied</td><td></td><td></td></tr><tr><td>Aftercare explained</td><td></td><td></td></tr><tr><td>Notes written in file</td><td></td><td></td></tr><tr><td>Review booked</td><td></td><td></td></tr>
    </table>
    <div class="signbox">Trainer Name: ____________<br>Signature: ____________ Date: ______</div>
    <div class="foot"><span class="n">Page 31</span><span class="g"></span></div></div>
</div>

<!-- ROW 5 -->
<div class="row" style="top:812px">
  <div class="page"><div class="head"><span class="num">12</span><span class="brand"><i class="brand-dot"></i>Velmora Training</span></div>
    <div class="mod-title">Extractions</div>
    <ul class="bullets">
      <li>Extractions clear blocked pores and are done during a facial treatment.</li>
      <li>Soften the skin first and use a sterile lancet only where needed.</li>
      <li>Never extract on inflamed or broken skin.</li>
    </ul>
    <div class="howto"><h4>How to finish this module</h4><ol><li>Read the manual section on extractions.</li><li>Watch your trainer on two clients.</li><li>Complete the sign off sheet.</li></ol></div>
    <div class="foot"><span class="n">Page 32</span><span class="g"></span></div></div>

  <div class="page"><div class="head"><span class="page-title">Extractions Sign Off</span><span class="brand"><i class="brand-dot"></i>Velmora Training</span></div>
    <div class="checks"><p>Observed trainer <span>Yes / No</span></p><p>Read manual <span>Yes / No</span></p><p>Watched video <span>Yes / No</span></p></div>
    <table class="sheet"><tr><th>Type</th><th>Date</th><th>Area</th><th>Tool</th><th>Sign</th></tr>
      <tr><td>Client 1</td><td></td><td></td><td></td><td></td></tr><tr><td>Client 2</td><td></td><td></td><td></td><td></td></tr><tr><td>Client 3</td><td></td><td></td><td></td><td></td></tr><tr><td>Client 4</td><td></td><td></td><td></td><td></td></tr><tr><td>Client 5</td><td></td><td></td><td></td><td></td></tr>
    </table>
    <div class="checks"><p>Approved to treat <span>Yes / No</span></p></div>
    <div class="signbox">Trainer Name: ____________<br>Signature: ____________ Date: ______</div>
    <div class="foot"><span class="n">Page 33</span><span class="g"></span></div></div>

  <div class="page"><div class="head"><span class="num">13</span><span class="brand"><i class="brand-dot"></i>Velmora Training</span></div>
    <div class="mod-title">LED Treatment</div>
    <ul class="bullets">
      <li>LED light therapy calms the skin and supports healing after treatments.</li>
      <li>Protective eyewear must be worn by the client at all times.</li>
      <li>Select the programme and time as set out in the treatment plan.</li>
    </ul>
    <div class="howto"><h4>How to finish this module</h4><ol><li>Read the manual section on LED.</li><li>Complete the sign off for three clients.</li></ol></div>
    <div class="checks" style="margin-top:4px"><p>Eyewear fitted <span>Yes / No</span></p><p>Settings recorded <span>Yes / No</span></p><p>Panel cleaned <span>Yes / No</span></p></div>
    <div class="signbox">Trainer: ____________ Date: ______</div>
    <div class="foot"><span class="n">Page 34</span><span class="g"></span></div></div>

  <div class="page"><div class="head"><span class="num">14</span><span class="brand"><i class="brand-dot"></i>Velmora Training</span></div>
    <div class="mod-title">Hair Removal</div>
    <ul class="bullets">
      <li>Laser hair removal targets the root of the hair to reduce regrowth.</li>
      <li>Check skin type and recent sun exposure before each session.</li>
      <li>Shave the area and test a small patch before the full treatment.</li>
      <li>Record all settings and any skin reaction in the client file.</li>
    </ul>
    <div class="howto"><h4>How to finish this module</h4><ol><li>Read the manual section on hair removal.</li><li>Watch the laser safety video.</li><li>Complete the sign off sheet.</li><li>Complete the hair removal form.</li></ol></div>
    <div class="foot"><span class="n">Page 35</span><span class="g"></span></div></div>

  <div class="page"><div class="head"><span class="page-title">Hair Removal Sign Off</span><span class="brand"><i class="brand-dot"></i>Velmora Training</span></div>
    <div class="staff">Staff Name:</div>
    <table class="sheet"><tr><th>Type</th><th>Date</th><th>Area</th><th>Settings</th><th>Sign</th></tr>
      <tr><td>Client 1</td><td></td><td></td><td></td><td></td></tr><tr><td>Client 2</td><td></td><td></td><td></td><td></td></tr><tr><td>Client 3</td><td></td><td></td><td></td><td></td></tr><tr><td>Client 4</td><td></td><td></td><td></td><td></td></tr><tr><td>Client 5</td><td></td><td></td><td></td><td></td></tr><tr><td>Client 6</td><td></td><td></td><td></td><td></td></tr><tr><td>Client 7</td><td></td><td></td><td></td><td></td></tr><tr><td>Client 8</td><td></td><td></td><td></td><td></td></tr>
    </table>
    <div class="checks"><p>Patch test done <span>Yes / No</span></p><p>Settings recorded <span>Yes / No</span></p></div>
    <div class="foot"><span class="n">Page 36</span><span class="g"></span></div></div>

  <div class="page"><div class="head"><span class="page-title">Hair Removal Form</span><span class="brand"><i class="brand-dot"></i>Velmora Training</span></div>
    <table class="sheet yn"><tr><th>Step</th><th>Y</th><th>N</th></tr>
      <tr><td>Consultation completed</td><td></td><td></td></tr><tr><td>Skin type assessed</td><td></td><td></td></tr><tr><td>Sun exposure checked</td><td></td><td></td></tr><tr><td>Area shaved</td><td></td><td></td></tr><tr><td>Eyewear on for all</td><td></td><td></td></tr><tr><td>Patch test done</td><td></td><td></td></tr><tr><td>Cooling gel applied</td><td></td><td></td></tr><tr><td>Settings recorded</td><td></td><td></td></tr><tr><td>Skin reaction noted</td><td></td><td></td></tr><tr><td>Aftercare explained</td><td></td><td></td></tr><tr><td>Handpiece cleaned</td><td></td><td></td></tr><tr><td>Next session booked</td><td></td><td></td></tr>
    </table>
    <div class="signbox">Trainer Name: ____________<br>Signature: ____________ Date: ______</div>
    <div class="foot"><span class="n">Page 37</span><span class="g"></span></div></div>

  <div class="page"><div class="head"><span class="num">15</span><span class="brand"><i class="brand-dot"></i>Velmora Training</span></div>
    <div class="mod-title">Broad Band Light</div>
    <ul class="bullets">
      <li>Broad band light treats redness, pigment and sun damage.</li>
      <li>Clients must avoid tanning for four weeks before treatment.</li>
      <li>Use the filter and energy shown in the client plan.</li>
      <li>Once you are confident, your trainer will observe three treatments.</li>
    </ul>
    <div class="howto"><h4>How to finish this module</h4><ol><li>Read the manual section on broad band light.</li><li>Complete the sign off sheet.</li><li>Complete the treatment form.</li></ol></div>
    <div class="foot"><span class="n">Page 38</span><span class="g"></span></div></div>

  <div class="page"><div class="head"><span class="page-title">BBL Sign Off</span><span class="brand"><i class="brand-dot"></i>Velmora Training</span></div>
    <div class="staff">Staff Name:</div>
    <table class="sheet"><tr><th>Type</th><th>Date</th><th>Filter</th><th>Energy</th><th>Sign</th></tr>
      <tr><td>Client 1</td><td></td><td></td><td></td><td></td></tr><tr><td>Client 2</td><td></td><td></td><td></td><td></td></tr><tr><td>Client 3</td><td></td><td></td><td></td><td></td></tr><tr><td>Client 4</td><td></td><td></td><td></td><td></td></tr><tr><td>Client 5</td><td></td><td></td><td></td><td></td></tr><tr><td>Client 6</td><td></td><td></td><td></td><td></td></tr><tr><td>Client 7</td><td></td><td></td><td></td><td></td></tr><tr><td>Client 8</td><td></td><td></td><td></td><td></td></tr>
    </table>
    <div class="checks"><p>Tanning checked <span>Yes / No</span></p><p>Settings recorded <span>Yes / No</span></p></div>
    <div class="foot"><span class="n">Page 39</span><span class="g"></span></div></div>
</div>

<!-- ROW 6 -->
<div class="row" style="top:996px">
  <div class="page"><div class="head"><span class="num">16</span><span class="brand"><i class="brand-dot"></i>Velmora Training</span></div>
    <div class="mod-title">Fractionated Laser</div>
    <ul class="bullets">
      <li>Fractionated laser resurfaces the skin to treat scars and fine lines.</li>
      <li>Apply numbing cream and check the client has stopped active products.</li>
      <li>Expect redness for several days; explain downtime clearly.</li>
    </ul>
    <div class="howto"><h4>How to finish this module</h4><ol><li>Read the manual section on laser.</li><li>Watch the laser safety video.</li><li>Complete the sign off sheet.</li><li>Complete the three laser forms.</li></ol></div>
    <div class="foot"><span class="n">Page 40</span><span class="g"></span></div></div>

  <div class="page"><div class="head"><span class="page-title">Laser Sign Off</span><span class="brand"><i class="brand-dot"></i>Velmora Training</span></div>
    <div class="staff">Staff Name:</div>
    <table class="sheet"><tr><th>Type</th><th>Date</th><th>Area</th><th>Depth</th><th>Sign</th></tr>
      <tr><td>Client 1</td><td></td><td></td><td></td><td></td></tr><tr><td>Client 2</td><td></td><td></td><td></td><td></td></tr><tr><td>Client 3</td><td></td><td></td><td></td><td></td></tr><tr><td>Client 4</td><td></td><td></td><td></td><td></td></tr><tr><td>Client 5</td><td></td><td></td><td></td><td></td></tr><tr><td>Client 6</td><td></td><td></td><td></td><td></td></tr><tr><td>Client 7</td><td></td><td></td><td></td><td></td></tr>
    </table>
    <div class="checks"><p>Numbing applied <span>Yes / No</span></p><p>Downtime explained <span>Yes / No</span></p></div>
    <div class="foot"><span class="n">Page 41</span><span class="g"></span></div></div>

  <div class="page"><div class="head"><span class="page-title">Laser Form 1</span><span class="brand"><i class="brand-dot"></i>Velmora Training</span></div>
    <div class="staff">Patient Name:</div>
    <table class="sheet yn"><tr><th>Pre-treatment</th><th>Y</th><th>N</th></tr>
      <tr><td>Consultation completed</td><td></td><td></td></tr><tr><td>Medical history reviewed</td><td></td><td></td></tr><tr><td>Active products stopped</td><td></td><td></td></tr><tr><td>Antiviral taken if needed</td><td></td><td></td></tr><tr><td>Consent signed</td><td></td><td></td></tr><tr><td>Photos taken</td><td></td><td></td></tr><tr><td>Numbing cream applied</td><td></td><td></td></tr><tr><td>Cream removed fully</td><td></td><td></td></tr><tr><td>Skin cleansed</td><td></td><td></td></tr><tr><td>Eyewear fitted</td><td></td><td></td></tr><tr><td>Test spot done</td><td></td><td></td></tr><tr><td>Settings checked</td><td></td><td></td></tr><tr><td>Room door signed</td><td></td><td></td></tr><tr><td>Smoke extractor on</td><td></td><td></td></tr>
    </table>
    <div class="tiny">Trainer: ____________ Date: ______</div>
    <div class="foot"><span class="n">Page 42</span><span class="g"></span></div></div>

  <div class="page"><div class="head"><span class="page-title">Laser Form 2</span><span class="brand"><i class="brand-dot"></i>Velmora Training</span></div>
    <div class="staff">Patient Name:</div>
    <table class="sheet yn"><tr><th>During treatment</th><th>Y</th><th>N</th></tr>
      <tr><td>Skin held taut</td><td></td><td></td></tr><tr><td>Passes overlapped evenly</td><td></td><td></td></tr><tr><td>Client comfort checked</td><td></td><td></td></tr><tr><td>Cooling air used</td><td></td><td></td></tr><tr><td>Number of passes noted</td><td></td><td></td></tr><tr><td>Energy recorded</td><td></td><td></td></tr><tr><td>Density recorded</td><td></td><td></td></tr><tr><td>Skin response noted</td><td></td><td></td></tr><tr><td>Soothing balm applied</td><td></td><td></td></tr><tr><td>Ice packs offered</td><td></td><td></td></tr><tr><td>Tip removed and discarded</td><td></td><td></td></tr><tr><td>Handpiece cleaned</td><td></td><td></td></tr><tr><td>Room reset</td><td></td><td></td></tr><tr><td>Notes written</td><td></td><td></td></tr><tr><td>Trainer reviewed notes</td><td></td><td></td></tr>
    </table>
    <div class="tiny">Trainer: ____________ Date: ______</div>
    <div class="foot"><span class="n">Page 43</span><span class="g"></span></div></div>

  <div class="page"><div class="head"><span class="page-title">Laser Form 3</span><span class="brand"><i class="brand-dot"></i>Velmora Training</span></div>
    <div class="staff">Patient Name:</div>
    <table class="sheet yn"><tr><th>Aftercare</th><th>Y</th><th>N</th></tr>
      <tr><td>Written aftercare given</td><td></td><td></td></tr><tr><td>Downtime explained</td><td></td><td></td></tr><tr><td>Sun protection advised</td><td></td><td></td></tr><tr><td>Make-up advice given</td><td></td><td></td></tr><tr><td>Follow up call booked</td><td></td><td></td></tr>
    </table>
    <div class="tiny">Trainer: ____________ Date: ______</div>
    <table class="sheet yn" style="margin-top:4px"><tr><th>Review</th><th>Y</th><th>N</th></tr>
      <tr><td>Healing on track</td><td></td><td></td></tr><tr><td>Review photos taken</td><td></td><td></td></tr><tr><td>Client satisfied</td><td></td><td></td></tr><tr><td>Next session planned</td><td></td><td></td></tr><tr><td>File updated</td><td></td><td></td></tr>
    </table>
    <div class="tiny">Trainer: ____________ Date: ______</div>
    <div class="foot"><span class="n">Page 44</span><span class="g"></span></div></div>

  <div class="page cover end">
    <div class="mark" role="img" aria-label="Velmora Training emblem area"></div>
    <div class="brand"><span>Velmora Training</span></div>
    <h1>Congratulations</h1>
    <p>You have completed all of the components of clinical treatments induction for the practice.</p>
    <p>We hope you enjoy your time working with us.</p>
    <svg width="126" height="56" viewBox="0 0 126 56"><path d="M0 20 Q60 46 126 8 V56 H0Z" fill="var(--gold)"/><path d="M0 28 Q62 54 126 16 V56 H0Z" fill="var(--navy)"/></svg>
  </div>
</div>

</body>
</html>
```